Author book launch promotion design for social media

We are organising an authors book launch event and require an author promotion design that will be used on social media (Chatterbook, netted) promotion.

The design must have the author's photo, image of their book, the event logo, details of the event plus website address (penfairhall.com.au).

Details of the event can be found at penfairhall.com.au.

the design has to be attractive and inviting and colours in accordance with the brand colours.

You can choose 1 one of the book images attached
Author name: Dr Tarek Bismil
Event Details
LAUNCH YOUR BOOK IN STYLE

Quillmark Reading Fair and Showcase 2022
7 - 8 October 2022
Melbourne Larkvale Centre
14 Corrigal St, Southbank Melbourne

For registration and ticketing visit:
penfairhall.com.au

I have attached also a sample promo. Please be creative.

```html
<!DOCTYPE html>
<html lang="en">
<head>
<meta charset="utf-8">
<title>Quillmark Reading Fair and Showcase 2022 – Promo</title>
<link rel="stylesheet" href="https://fonts.googleapis.com/css2?family=Bebas+Neue&family=Montserrat:wght@300;400;500;600;700;800&display=swap">
<style>
  :root{
    --navy:#0c3455;
    --navy-deep:#082a47;
    --gold:#c9a13b;
    --gold-light:#e6c766;
    --white:#ffffff;
    --page:#ffffff;
    --cover-top:#eef0f3;
    --cover-mid:#b9c2ce;
    --cover-low:#2c3e66;
    --page-edge:#f3f3f3;
    --spine-red:#c8263a;
  }
  *{box-sizing:border-box;margin:0;padding:0}
  html,body{width:1200px;height:2192px;overflow:hidden;background:var(--page)}
  .promo{
    position:absolute;left:60px;top:556px;width:1080px;height:1080px;overflow:hidden;
    background:linear-gradient(160deg,var(--navy) 0%,var(--navy-deep) 100%);
    font-family:'Montserrat',sans-serif;color:var(--white);
    box-shadow:0 20px 50px rgba(0,0,0,.25);
  }
  .promo__bands{position:absolute;inset:0}
  .brand{position:absolute;left:84px;top:58px;display:flex;align-items:center;gap:14px}
  .brand__mark{width:34px;height:34px;border-radius:50%;background:var(--gold)}
  .brand__name{font-weight:700;font-size:44px;color:var(--gold);letter-spacing:1px}
  .tagline{position:absolute;right:82px;top:58px;text-align:right;padding-right:24px;border-right:4px solid var(--gold);line-height:1.05}
  .tagline__lead{display:block;font-weight:400;font-size:41px;letter-spacing:1.5px}
  .tagline__strong{display:block;font-weight:800;font-size:40px;color:var(--gold);letter-spacing:1px}
  .author-photo{position:absolute;left:560px;top:180px;width:520px;height:660px;
    background:radial-gradient(ellipse at 55% 30%,#b88368 0%,#5a3a2c 22%,#2a2a30 45%,#1c1f26 100%);
    border-radius:200px 200px 0 0;}
  .headline{position:absolute;left:80px;top:226px;font-family:'Bebas Neue',sans-serif;font-weight:400;font-size:104px;line-height:.9;letter-spacing:.5px;z-index:2}
  .headline__line{display:block}
  .headline__line--gold{color:var(--gold)}
  .rule{position:absolute;left:82px;top:522px;width:52px;height:4px;background:var(--gold)}
  .dates{position:absolute;left:80px;top:540px;display:flex;align-items:center;gap:22px}
  .dates__days{font-family:'Bebas Neue',sans-serif;font-size:92px;line-height:1}
  .dates__days sup{font-size:48px;vertical-align:36px}
  .dates__month{font-weight:600;font-size:41px;color:var(--gold);line-height:.95;letter-spacing:1px}
  .speaker{position:absolute;left:74px;top:686px;width:560px;height:90px;z-index:3}
  .speaker__name{position:absolute;left:30px;top:0;height:90px;display:flex;align-items:center;
    font-weight:800;font-size:44px;color:var(--gold);letter-spacing:1.5px}
  .venue{position:absolute;left:88px;top:806px;display:flex;gap:14px;color:var(--navy);z-index:3}
  .venue__text{font-weight:500;font-size:27px;line-height:1.3;letter-spacing:.3px}
  .dots{position:absolute;left:88px;top:900px;display:flex;gap:6px;z-index:3}
  .dots span{width:8px;height:8px;border-radius:50%;background:var(--white)}
  .dots span:last-child{opacity:.5}
  .register{position:absolute;left:80px;top:930px;font-weight:700;font-size:26px;color:var(--navy);letter-spacing:.6px;z-index:3}
  .web{position:absolute;left:76px;top:972px;height:68px;width:664px;z-index:3}
  .web__bar{position:absolute;left:30px;top:6px;right:0;height:56px;background:var(--navy)}
  .web__icon{position:absolute;left:0;top:0;width:68px;height:68px}
  .web__url{position:absolute;left:92px;top:6px;height:56px;display:flex;align-items:center;font-weight:600;font-size:36px;letter-spacing:.5px}

  .book{position:absolute;left:667px;top:624px;width:398px;height:418px;z-index:4}
  .book__cover{position:absolute;left:73px;top:0;width:225px;height:366px;
    background:linear-gradient(180deg,var(--cover-top) 0%,var(--cover-mid) 45%,var(--cover-low) 88%);
    box-shadow:6px 0 0 #d9dde3,0 8px 18px rgba(0,0,0,.3)}
  .book__flat{position:absolute;left:0;top:366px;width:398px;height:48px;
    background:linear-gradient(180deg,var(--page-edge) 0%,var(--page-edge) 55%,var(--spine-red) 55%,#a51d2f 100%);
    box-shadow:0 8px 16px rgba(0,0,0,.25)}
</style>
</head>
<body>
<article class="promo">
  <svg class="promo__bands" viewBox="0 0 1080 1080" preserveAspectRatio="none" aria-hidden="true">
    <defs>
      <linearGradient id="goldFill" x1="0" y1="0" x2="1" y2="1">
        <stop offset="0" stop-color="#c79a34"/>
        <stop offset=".55" stop-color="#d9b550"/>
        <stop offset="1" stop-color="#ecd173"/>
      </linearGradient>
    </defs>
    <polygon points="0,618 1080,880 1080,1080 0,1080" fill="url(#goldFill)"/>
  </svg>

  <div class="author-photo" role="img" aria-label="Portrait photo of author Dr Tarek Bismil in a dark suit"></div>

  <svg class="promo__bands" viewBox="0 0 1080 1080" preserveAspectRatio="none" aria-hidden="true" style="z-index:1">
    <defs>
      <linearGradient id="goldFill2" x1="0" y1="0" x2="1" y2="1">
        <stop offset="0" stop-color="#c79a34"/>
        <stop offset=".55" stop-color="#d9b550"/>
        <stop offset="1" stop-color="#ecd173"/>
      </linearGradient>
    </defs>
    <polygon points="0,618 470,736 980,860 1080,800 1080,1080 0,1080" fill="#ffffff"/>
    <polygon points="0,640 450,748 980,878 1080,822 1080,1080 0,1080" fill="url(#goldFill2)"/>
  </svg>

  <div class="brand"><span class="brand__mark"></span><span class="brand__name">QUILLMARK</span></div>

  <p class="tagline"><span class="tagline__lead">LAUNCH YOUR BOOK</span><span class="tagline__strong">IN STYLE</span></p>

  <h1 class="headline">
    <span class="headline__line">QUILLMARK</span>
    <span class="headline__line">READING FAIR AND</span>
    <span class="headline__line headline__line--gold">SHOWCASE 2022</span>
  </h1>

  <div class="rule"></div>
  <div class="dates">
    <span class="dates__days">7<sup>TH</sup> - 8<sup>TH</sup></span>
    <span class="dates__month">OCTOBER<br>2022</span>
  </div>

  <div class="speaker">
    <svg viewBox="0 0 560 90" width="560" height="90" aria-hidden="true">
      <path d="M45,3 H510 L552,45 L510,87 H45 A42,42 0 0 1 45,3 Z" fill="#c9a13b"/>
      <path d="M45,9 H500 L530,45 L500,81 H45 A36,36 0 0 1 45,9 Z" fill="#0c3455"/>
    </svg>
    <span class="speaker__name">DR. TAREK BISMIL</span>
  </div>

  <div class="venue">
    <svg width="20" height="64" viewBox="0 0 20 64" aria-hidden="true">
      <path d="M10 1a8 8 0 0 0-8 8c0 6 8 15 8 15s8-9 8-15a8 8 0 0 0-8-8zm0 11a3 3 0 1 1 0-6 3 3 0 0 1 0 6z" fill="#0c3455"/>
      <circle cx="10" cy="34" r="1.6" fill="#0c3455"/><circle cx="10" cy="42" r="1.6" fill="#0c3455"/>
      <circle cx="10" cy="52" r="3" fill="#0c3455"/>
    </svg>
    <p class="venue__text">Melbourne Larkvale Centre<br>14 Corrigal St, Southbank Melbourne</p>
  </div>

  <div class="dots"><span></span><span></span><span></span><span></span></div>

  <p class="register">FOR REGISTRATION AND TICKETING VISIT:</p>

  <div class="web">
    <div class="web__bar"></div>
    <svg class="web__icon" viewBox="0 0 68 68" aria-hidden="true">
      <circle cx="34" cy="34" r="32" fill="#0c3455" stroke="#e6c766" stroke-width="4"/>
      <path d="M22 46 L44 24 L38 48 L33 37 Z" fill="#ffffff"/>
    </svg>
    <span class="web__url">penfairhall.com.au</span>
  </div>

  <div class="book" role="img" aria-label="Photo of the author's book, one copy standing and one lying flat">
    <div class="book__cover"></div>
    <div class="book__flat"></div>
  </div>
</article>
</body>
</html>
```